Flyer for spiritual retreat (yoga, meditation, reiki, raw food)

I would like a flyer to promote my upcoming retreat and a matching Facebook banner.

The name of the retreat is "Wavecrest Of Calm" and the tagline is "retreat into you"

The activities in the retreat include daily meditation, ecstatic dance, spiritual development workshops on intuition, energy healing etc and a reiki session is included.

I would like a flyer designed to promote this, something that is editable as I will be running this multiple times and will need to adjust the flyer to add the dates etc each time.

edit: add that here will be fully catered raw food and juices, and that the retreat price includes all accomodation, meals and workshops.

Please contact me if you need further info. Please also visit my website www.marithovland.com and www.facebook.com/tolvanahaven to see my current events and promotions.

Thank you,

Marit

Reason: Hi all, thank you all for your submissions. Apologies as I am traveling and do not have much access to internet and will review your submissions and provide feedback as soon as possible. Kind regards, Marit.

Target Market(s)

People who like meditation, yoga, fans of rowan mabry and jasper vinek, those interested in personal and spiritual development.

Industry/Entity Type

Health And Wellness

Requirements
Must have
• Please put the included reiki session as as added bonus. Something like "BONUS 30 minute reiki healing session" in a little star/banner/something that stands out.
• Please emphasise the "light" part of Wavecrest as I am going for a play on words between in the light and enlightenment.
• Please include placeholder text for place, location, time
• Placeholder for price
• My name (see attached file - can change colour to suit) and website (www.marithovland.com)
Nice to have
• I prefer rounded designs, curves rather than block designs.
Should not have
• Tolvana Haven logo

```html
<!DOCTYPE html>
<html lang="en">
<head>
<meta charset="utf-8">
<title>Wavecrest Of Calm – Retreat Flyer</title>
<link rel="stylesheet" href="https://fonts.googleapis.com/css2?family=Montserrat:wght@300;700&family=Cormorant+Garamond:ital,wght@1,600&family=Questrial&family=Oswald:wght@500;700&family=Lato:ital,wght@0,700;1,700&family=Noto+Serif:wght@700&family=Great+Vibes&display=swap">
<style>
  :root {
    --green: #5b9f1c;
    --green-light: #7cc242;
    --green-dark: #3f7a0e;
    --charcoal: #474747;
    --ink: #1d1d1d;
    --white: #ffffff;
    --canvas: #ececec;
    --sun-top: #f7c23a;
    --sun-mid: #e79512;
    --sun-deep: #6b3a08;
  }
  * { margin: 0; padding: 0; box-sizing: border-box; }
  html, body { width: 1200px; height: 1200px; overflow: hidden; background: var(--canvas); }
  .flyer {
    position: absolute; left: 194px; top: 30px;
    width: 812px; height: 1140px; overflow: hidden;
    background: var(--white);
    box-shadow: 0 6px 24px rgba(0,0,0,.25);
  }
  .flyer-shapes { position: absolute; inset: 0; }
  .flyer > div, .flyer > p, .flyer > ul { position: absolute; }

  .tagline { left: 78px; top: 84px; font-size: 58px; line-height: 1; white-space: nowrap; }
  .tagline-strong { font-family: "Montserrat", sans-serif; font-weight: 700; color: var(--green); letter-spacing: 1px; }
  .tagline-soft { font-family: "Montserrat", sans-serif; font-weight: 300; color: var(--white); margin-left: 10px; }

  .title-main {
    left: 66px; top: 150px; font-family: "Cormorant Garamond", serif; font-style: italic; font-weight: 600;
    font-size: 104px; color: var(--white); letter-spacing: 2px;
    text-shadow: 0 2px 6px rgba(90,40,0,.55);
  }
  .title-sub {
    left: 0; width: 574px; top: 276px; text-align: center;
    font-family: "Questrial", sans-serif; font-size: 64px; color: var(--white);
    text-shadow: 0 2px 4px rgba(90,40,0,.4);
  }

  .bonus { left: 483px; top: 376px; width: 316px; height: 316px; text-align: center; }
  .bonus-word {
    margin-top: 74px; font-family: "Oswald", sans-serif; font-weight: 700; font-size: 80px; line-height: .95;
    color: var(--green); -webkit-text-stroke: 2px var(--ink); letter-spacing: 1px;
  }
  .bonus-time { font-family: "Oswald", sans-serif; font-weight: 700; font-size: 54px; line-height: 1; color: var(--ink); }
  .bonus-detail { font-family: "Oswald", sans-serif; font-weight: 500; font-size: 30px; line-height: 1.2; color: var(--ink); }

  .host-name {
    left: 50px; top: 518px; font-family: "Great Vibes", cursive; font-size: 72px; line-height: 1;
    color: var(--green-light); -webkit-text-stroke: 1px var(--green-dark); white-space: nowrap;
  }

  .activities-label {
    left: 67px; top: 641px; width: 280px; height: 31px; background: var(--green);
    color: var(--white); font-family: "Lato", sans-serif; font-style: italic; font-weight: 700;
    font-size: 16px; line-height: 31px; text-align: center;
  }
  .activities { list-style: none; font-family: "Questrial", sans-serif; font-size: 18px; line-height: 21px; color: #2b2b2b; }
  .activities li { padding-left: 16px; position: relative; }
  .activities li::before {
    content: ""; position: absolute; left: 0; top: 8px; width: 7px; height: 7px; border-radius: 50%; background: var(--green);
  }
  .activities-a { left: 57px; top: 692px; }
  .activities-b { left: 231px; top: 692px; }

  .more-info {
    right: 50px; top: 722px; text-align: right; font-family: "Noto Serif", serif; font-weight: 700;
    font-size: 17px; line-height: 22px; color: var(--ink);
  }
  .more-info-rule { display: inline-block; width: 96px; height: 2px; background: var(--green); vertical-align: middle; margin-right: 4px; }
  .website-bar {
    left: 519px; top: 772px; width: 293px; height: 28px; background: var(--green);
    font-family: "Oswald", sans-serif; font-weight: 500; font-size: 20px; line-height: 28px;
    color: var(--white); padding-left: 12px; letter-spacing: .3px;
  }

  .inclusions {
    left: 39px; top: 1024px; font-family: "Lato", sans-serif; font-weight: 700;
    font-size: 17px; line-height: 21px; color: var(--white); white-space: nowrap;
  }
  .event-details {
    left: 39px; top: 1098px; font-family: "Lato", sans-serif; font-weight: 700;
    font-size: 14px; line-height: 18px; color: var(--green-light); white-space: nowrap;
  }
</style>
</head>
<body>
<main class="flyer">
  <svg class="flyer-shapes" viewBox="0 0 812 1140" width="812" height="1140">
    <defs>
      <linearGradient id="sunset" x1="0" y1="0" x2="0.7" y2="1">
        <stop offset="0" stop-color="var(--sun-top)"/>
        <stop offset=".45" stop-color="var(--sun-mid)"/>
        <stop offset="1" stop-color="var(--sun-deep)"/>
      </linearGradient>
      <radialGradient id="sunGlow" cx=".72" cy=".12" r=".5">
        <stop offset="0" stop-color="#fff4c4" stop-opacity=".9"/>
        <stop offset="1" stop-color="#fff4c4" stop-opacity="0"/>
      </radialGradient>
      <linearGradient id="softWhite" x1="0" y1="0" x2="0" y2="1">
        <stop offset="0" stop-color="#ffffff"/>
        <stop offset="1" stop-color="#f0f0f0"/>
      </linearGradient>
      <linearGradient id="shoreGlow" x1="0" y1="0" x2="0" y2="1">
        <stop offset="0" stop-color="#e9b26a"/>
        <stop offset=".55" stop-color="#c7806b"/>
        <stop offset="1" stop-color="#6c5d63"/>
      </linearGradient>
      <linearGradient id="duskGlow" x1="0" y1="0" x2="0" y2="1">
        <stop offset="0" stop-color="#f4b324"/>
        <stop offset=".6" stop-color="#d07a0c"/>
        <stop offset="1" stop-color="#2a1a08"/>
      </linearGradient>
      <linearGradient id="juiceTones" x1="0" y1="0" x2="1" y2="0">
        <stop offset="0" stop-color="#9fd24a"/>
        <stop offset=".3" stop-color="#ef5a4e"/>
        <stop offset=".6" stop-color="#f8a21c"/>
        <stop offset="1" stop-color="#d9e25c"/>
      </linearGradient>
    </defs>

    <rect width="812" height="1140" fill="url(#softWhite)"/>

    <g role="img" aria-label="Photo: woman meditating in lotus pose on a beach at golden sunset">
      <path d="M0 0 H812 V462 Q430 500 0 346 Z" fill="url(#sunset)"/>
      <path d="M0 0 H812 V462 Q430 500 0 346 Z" fill="url(#sunGlow)"/>
    </g>
    <path d="M0 346 Q300 455 560 474 L812 464 L812 480 Q430 515 0 366 Z" fill="var(--green)"/>

    <line x1="80" y1="273" x2="500" y2="273" stroke="#ffffff" stroke-opacity=".7" stroke-width="1.5"/>

    <path d="M0 966 Q280 1025 520 1006 Q680 990 812 852 V1140 H0 Z" fill="var(--charcoal)"/>

    <circle cx="641" cy="533" r="155" fill="var(--white)" stroke="var(--green)" stroke-width="7"/>

    <g role="img" aria-label="Photo: silhouette in yoga pose on a shoreline at dusk">
      <circle cx="147" cy="885" r="83" fill="url(#shoreGlow)"/>
    </g>
    <circle cx="147" cy="885" r="83" fill="none" stroke="var(--green)" stroke-width="5"/>
    <g role="img" aria-label="Photo: meditating hand silhouetted against the setting sun">
      <circle cx="353" cy="885" r="83" fill="url(#duskGlow)"/>
    </g>
    <circle cx="353" cy="885" r="83" fill="none" stroke="var(--green)" stroke-width="5"/>

    <g role="img" aria-label="Illustration: glasses of fresh juice with sliced citrus fruits">
      <rect x="478" y="840" width="316" height="290" rx="40" fill="url(#juiceTones)" opacity=".9"/>
    </g>
  </svg>

  <div class="tagline"><span class="tagline-strong">Retreat</span><span class="tagline-soft">into you</span></div>
  <div class="title-main">Wavecrest</div>
  <div class="title-sub">Of Calm</div>

  <div class="bonus">
    <div class="bonus-word">BONUS</div>
    <div class="bonus-time">30 minute</div>
    <div class="bonus-detail">reiki healing session</div>
  </div>

  <div class="host-name">Marit Hovland</div>

  <div class="activities-label">The activities in the retreat include.</div>
  <ul class="activities activities-a">
    <li>daily meditation</li>
    <li>ecstatic dance</li>
    <li>energy healing</li>
  </ul>
  <ul class="activities activities-b">
    <li>spiritual development<br>workshops on intuition</li>
  </ul>

  <div class="more-info">For more information<br><span class="more-info-rule"></span>visit my website</div>
  <div class="website-bar">www.marithovland.com</div>

  <p class="inclusions">Here will be fully catered raw food andjuices, and<br>that the retreat price includes all accomodation,<br>meals and workshops.</p>
  <p class="event-details">Date: TBA · Time: TBA · Place: TBA · Price: TBA</p>
</main>
</body>
</html>
```